Letterhead Design for Law Firm

**Edit: I have added the photo of a bottom that I like.

------
We are looking for a re-design of our new letterhead. The letterhead is for a law firm and will be used for digital and traditionally printed correspondence.

Here are some suggestions:

- Please use colours are #8ec900 and simple black.
- Please do not use any type of "waves" at the bottom of the page. This is not in style at all.
- Please stay modern yet conservative.
- Please use font Segoe UI Light or similar if you can
- Avoid clipart or illustrations.
- Utilize ample white space in the layout so the design looks clean and information is easy to read at a glance. Don't overcrowd the letterhead.
- Make sure the letterhead design is consistent with our brand identity (see brambleford.ca)
-Please, no black headers or footers.

I am attaching my current letterhead and signature for your convenience.

Remember, the letterhead is an extension of our professional identity. We are a successful firm and trial lawyers who correspond with insurers, judges, lawyers, courts, clients, etc. Make it new, modern, attractive, yet powerful and conservative.

It needs to be easily printable. I would like the bleed removed in print so the black bar the bottom crosses the page (but the text is not near the edges)

Target Market(s)

Clients, Government Offices, Judiciary, Lawyers, Insurance Companies, Colleagues.

Industry/Entity Type

Law

Font styles to use
Other font styles liked:
• Segoe UI LIght, Calibri Light,

Colors
00AB8E
00BBA5
67D7C9
C6EFE9
E9F9F6

Requirements
Must have
• Everything that is on the letterhead now.
Nice to have
• Cutting Edge design, yet conservative.
Should not have
• law firm cliche design, images,

```html
<!DOCTYPE html>
<html lang="en">
<head>
<meta charset="utf-8">
<title>Brambleford Letterhead</title>
<link href="https://fonts.googleapis.com/css2?family=Roboto:wght@300;400;500;700&display=swap" rel="stylesheet">
<style>
:root{
  --paper:#f5f2f3;
  --ink:#1c1c1c;
  --text:#3a3a3a;
  --muted:#555555;
  --green:#9fd15b;
  --footer-black:#1e1e1e;
  --rule:#4a4a4a;
  --icon-green:#7cbf3a;
}
*{margin:0;padding:0;box-sizing:border-box}
html,body{width:935px;height:1200px;overflow:hidden;background:var(--paper)}
body{font-family:"Roboto",Arial,sans-serif;color:var(--text);position:relative}
.abs{position:absolute}

.brand-rule{left:339px;width:279px;height:2px;background:var(--green)}
.brand-name{left:0;width:935px;top:62px;text-align:center;font-size:21px;font-weight:400;color:var(--ink);line-height:26px}

.label{font-weight:500;color:var(--ink);font-size:15.5px}
.meta{font-size:15.5px;color:var(--muted)}
.right{right:64px;text-align:right}

.address{left:42px;top:236px;font-size:16px;line-height:20px;color:var(--ink);font-weight:400;font-style:normal}
.attn{left:42px;font-size:16px;color:var(--ink)}
.re-label{left:42px;top:428px}
.re-block{left:326px;top:426px;font-size:16px;line-height:20px;color:var(--ink)}
.divider{left:53px;top:520px;width:818px;height:1px;background:var(--rule)}

.body-copy{left:53px;top:543px;width:818px;font-family:Arial,"Roboto",sans-serif;font-size:14.6px;line-height:20.5px;text-align:justify;color:#4a4a4a}
.body-copy p{margin-bottom:20px}

.closing{left:56px;top:842px;font-size:15px;line-height:18px;color:var(--ink)}
.signature{left:56px;top:892px;width:258px;height:52px;background:linear-gradient(90deg,rgba(0,0,0,0.08),rgba(0,0,0,0.03))}
.signer{left:59px;top:962px;font-size:15px;line-height:18px;color:var(--ink)}

.contact{left:63px;top:1074px;font-size:14.5px;line-height:20px;color:var(--ink)}
.contact li{list-style:none;display:flex;align-items:center;gap:8px}
.contact svg{width:14px;height:14px;flex:none}
.practice{right:39px;top:1081px;text-align:right;font-size:15px;line-height:19px;color:var(--muted)}
.practice strong{font-weight:500;color:var(--ink)}

.footer-bar{left:0;top:1158px;width:604px;height:42px;background:var(--footer-black);color:#fff;font-size:16px;display:flex;align-items:center;padding-left:56px}
.footer-web{left:608px;top:1158px;width:327px;height:42px;background:var(--green);color:var(--ink);font-size:15.5px;font-weight:500;display:flex;align-items:center;justify-content:center}
</style>
</head>
<body>
<header>
  <div class="abs brand-rule" style="top:42px"></div>
  <div class="abs brand-name">Brambleford Personal Injury Lawyers</div>
  <div class="abs brand-rule" style="top:108px"></div>
</header>

<div class="abs label" style="left:42px;top:140px">Without Prejudice</div>
<div class="abs right meta" style="top:144px"><span class="label">File Clerk:</span> Clara Whitmore</div>
<div class="abs label" style="left:42px;top:189px">By Email</div>
<div class="abs right meta" style="top:197px;font-size:14.5px;color:var(--ink)">March 13, 2024</div>

<address class="abs address">
  Northgate Insurance Company<br>
  Claims Litigation Department<br>
  240 Orchard Lane North<br>
  P.O. Box 3100<br>
  Elmvale, ON &nbsp; N0L 2K7
</address>

<div class="abs attn" style="top:353px">Attention:&nbsp; Mr. Dorian Pike</div>
<div class="abs attn" style="top:382px">Mr. Pike:</div>

<div class="abs label re-label">Re:</div>
<div class="abs re-block">
  Marlowe v. Castell et al.<br>
  DOL:&nbsp; September 12, 2019<br>
  Pre-Mediation Settlement Proposal – March 13th, 2024
</div>

<div class="abs divider"></div>

<div class="abs body-copy">
  <p>Lorem ipsum dolor sit amet, consectetur adipiscing elit. Donec orci purus, luctus vitae dignissim eu, iaculis sed purus. Vivamus faucibus, ipsum nec aliquet viverra, leo mauris condimentum ligula, sit amet sagittis enim ligula quis arcu. Nam egestas tortor ivisi porttitor mattis. In tortor ante, ultricies in suscipit a, tempus non massa. Vivamus et auctor mi. Fusce vel massa nulla. Phasellus nec eros mauris, et scelerisque orci.</p>
  <p>Donec malesuada orci vitae nulla accumsan porta a id massa. Quisque accumsan iaculis magna sit amet fringilla. Maecenas consequat, magna eget tincidunt semper, odio nibh rutrum mi, id feugiat ante nisi eu risus. Vestibulum nunc orci, rhoncus a placerat in, ultricies in mi. Cras mattis varius eros, vel fringilla nisi suscipit eget. Quisque scelerisque sagittis nulla at porttitor.</p>
  <p>Sed id augue vitae urna euismod commodo aliquet a quam. Pellentesque arcu velit, cursus et malesuada ut, consequat et diam. Nullam erat sem, rhoncus id ullamcorper vitae, rhoncus et arcu. In ultricies ultricies nulla, ut rutrum nisi iaculis</p>
</div>

<div class="abs closing">Yours very truly,<br>BRAMBLEFORD PERSONAL INJURY LAWYERS</div>
<div class="abs signature" role="img" aria-label="Handwritten signature of Owen R. Brambleford"></div>
<div class="abs signer">Owen R. Brambleford<br>Brambleford Law Professional Corporation<br>/cw<br>Encl.</div>

<ul class="abs contact">
  <li><svg viewBox="0 0 16 16"><path fill="var(--icon-green)" d="M3.6 1.2l2.3 2.4-1.3 2c.8 1.9 2.5 3.6 4.3 4.4l2-1.3 2.4 2.3-1.3 2.6C7 13.4 2.6 9 1 3z"/></svg>905-555-0142</li>
  <li><svg viewBox="0 0 16 16"><rect x="4" y="1.5" width="8" height="4" fill="var(--icon-green)"/><rect x="1.5" y="6" width="13" height="6" rx="1" fill="var(--icon-green)"/><rect x="4" y="10" width="8" height="4.5" fill="#cfe8a8"/></svg>905-555-0187</li>
  <li><svg viewBox="0 0 16 16"><rect x="1.5" y="3.5" width="13" height="9" fill="var(--icon-green)"/><path d="M1.5 3.5L8 9l6.5-5.5" fill="none" stroke="#fff" stroke-width="1.2"/></svg>Email: clara@brambleford.ca</li>
</ul>

<div class="abs practice">
  <strong>Practice Restricted-</strong> Serious Personal Injury, Wrongful Death Litigation<br>
  Long-Term Disability Litigation, Wrongful Dismissal Litigation<br>
  Employee Terminations
</div>

<footer>
  <div class="abs footer-bar">18 Harbour Street E., Suite 902, Lakeport, ON&nbsp; L9R 2B6</div>
  <div class="abs footer-web">www.BRAMBLEFORD.ca</div>
</footer>
</body>
</html>
```